Flyer-Design (plus Facebook Titelbild Größe) für Morgenrot Tattoo Festival
Zielgruppe
Tattoo Convention
Aufgabenstellung
Morgenrot Tattoo Festival
Sindelfingen
Samstag 12-23 Uhr Sonntag 12-20 Uhr
Messe Wolkenbach
Tattoos Piercings Shows

```html
<!DOCTYPE html>
<html lang="de">
<head>
<meta charset="utf-8">
<title>Morgenrot Tattoo Festival – Flyer und Titelbild</title>
<link rel="stylesheet" href="https://fonts.googleapis.com/css2?family=Anton&family=Bebas+Neue&family=Kalam:wght@700&family=Open+Sans:wght@600;700&display=swap">
<style>
  :root {
    --page: #ffffff;
    --ink: #000000;
    --white: #ffffff;
    --pink-a: #ff4f6a;
    --pink-b: #e0186f;
    --grey-a: #d9d9d9;
    --grey-b: #8a8a8a;
    --red: #c81e32;
    --skin-a: #3a1d14;
    --skin-b: #8a5a45;
  }
  * { margin: 0; padding: 0; box-sizing: border-box; }
  html, body { width: 1200px; height: 2747px; overflow: hidden; background: var(--page); }
  .canvas { position: relative; width: 1200px; height: 2747px; }

  .flyer {
    position: absolute; left: 308px; width: 565px; height: 792px;
    background: var(--ink); overflow: hidden;
    box-shadow: 0 6px 18px rgba(0,0,0,.25);
  }
  .flyer--first { top: 111px; }
  .flyer--second { top: 1175px; }

  .title {
    position: absolute; font-family: "Anton", sans-serif;
    background: linear-gradient(90deg, var(--pink-a), var(--pink-b));
    -webkit-background-clip: text; background-clip: text; color: transparent;
    letter-spacing: -1px; line-height: 1; white-space: nowrap;
  }
  .subtitle {
    position: absolute; font-family: "Kalam", cursive; font-weight: 700;
    background: linear-gradient(180deg, var(--grey-a), var(--grey-b));
    -webkit-background-clip: text; background-clip: text; color: transparent;
    line-height: 1; white-space: nowrap; letter-spacing: 2px;
  }
  .flyer .title { left: 55px; top: 48px; font-size: 80px; }
  .flyer .subtitle { left: 55px; top: 122px; font-size: 60px; }

  .photo {
    position: absolute;
    background: radial-gradient(ellipse at 55% 55%, var(--skin-b), var(--skin-a) 60%, var(--ink) 100%);
  }
  .flyer .photo { left: 285px; top: 215px; width: 280px; height: 450px; }

  .date-badge { position: absolute; }
  .flyer .date-badge { left: 40px; top: 346px; width: 222px; height: 220px; }
  .date-badge svg { position: absolute; inset: 0; width: 100%; height: 100%; }
  .date-text {
    position: absolute; color: var(--white); text-align: center; line-height: 1;
  }
  .date-month { font-family: "Bebas Neue", sans-serif; }
  .date-days, .date-year { font-family: "Open Sans", sans-serif; font-weight: 700; }
  .flyer .date-month { left: 0; width: 230px; top: 22px; font-size: 40px; }
  .flyer .date-days { left: 0; width: 230px; top: 58px; font-size: 46px; }
  .flyer .date-year { left: 0; width: 230px; top: 108px; font-size: 31px; font-weight: 600; }

  .venue, .program, .hours {
    position: absolute; color: var(--white); font-family: "Bebas Neue", sans-serif;
    text-align: center; line-height: 1; white-space: nowrap;
  }
  .flyer .venue { left: 0; width: 600px; top: 636px; font-size: 60px; }
  .flyer .program { left: 0; width: 605px; top: 696px; font-size: 38px; }
  .flyer .hours { left: 0; width: 600px; top: 735px; font-size: 34px; }

  .cover {
    position: absolute; left: 308px; top: 2060px; width: 565px; height: 209px;
    background: var(--ink); overflow: hidden;
    box-shadow: 0 6px 18px rgba(0,0,0,.25);
  }
  .cover .title { left: 24px; top: 22px; font-size: 50px; }
  .cover .subtitle { left: 24px; top: 74px; font-size: 38px; letter-spacing: 1px; }
  .cover .photo { left: 345px; top: 0; width: 220px; height: 209px; }
  .cover .date-badge { left: 22px; top: 128px; width: 80px; height: 64px; }
  .cover .date-month { left: 6px; top: 8px; font-size: 13px; text-align: left; }
  .cover .date-days { left: 6px; top: 22px; font-size: 21px; text-align: left; }
  .cover .date-year { left: 12px; top: 46px; font-size: 11px; text-align: left; }
  .cover .venue { left: 105px; width: 220px; top: 126px; font-size: 28px; }
  .cover .program { left: 105px; width: 220px; top: 156px; font-size: 18px; }
  .cover .hours { left: 105px; width: 220px; top: 176px; font-size: 16px; }
</style>
</head>
<body>
<main class="canvas">

  <section class="flyer flyer--first" aria-label="Flyer Morgenrot Tattoo Festival">
    <div class="photo" role="img" aria-label="Foto: tätowierter Rücken eines Mannes mit großem Flügelmotiv"></div>
    <h1 class="title">MORGENROT</h1>
    <p class="subtitle">Tattoo Festival</p>
    <div class="date-badge">
      <svg viewBox="0 0 222 220" aria-hidden="true"><polygon points="0,0 222,0 118,220" fill="var(--red)"/></svg>
      <div class="date-text date-month">FEB</div>
      <div class="date-text date-days">18-23</div>
      <div class="date-text date-year">2020</div>
    </div>
    <p class="venue">MESSE WOLKENBACH</p>
    <p class="program">TATTOOS PIERCINGS SHOWS</p>
    <p class="hours">SAMSTAG 12-23 UHR SONNTAG 12-20 UHR</p>
  </section>

  <section class="flyer flyer--second" aria-label="Flyer Morgenrot Tattoo Festival">
    <div class="photo" role="img" aria-label="Foto: tätowierter Rücken eines Mannes mit großem Flügelmotiv"></div>
    <h2 class="title">MORGENROT</h2>
    <p class="subtitle">Tattoo Festival</p>
    <div class="date-badge">
      <svg viewBox="0 0 222 220" aria-hidden="true"><polygon points="0,0 222,0 118,220" fill="var(--red)"/></svg>
      <div class="date-text date-month">FEB</div>
      <div class="date-text date-days">18-23</div>
      <div class="date-text date-year">2020</div>
    </div>
    <p class="venue">MESSE WOLKENBACH</p>
    <p class="program">TATTOOS PIERCINGS SHOWS</p>
    <p class="hours">SAMSTAG 12-23 UHR SONNTAG 12-20 UHR</p>
  </section>

  <section class="cover" aria-label="Titelbild Morgenrot Tattoo Festival">
    <div class="photo" role="img" aria-label="Foto: tätowierter Rücken eines Mannes mit großem Flügelmotiv"></div>
    <h2 class="title">MORGENROT</h2>
    <p class="subtitle">Tattoo Festival</p>
    <div class="date-badge">
      <svg viewBox="0 0 80 64" aria-hidden="true"><polygon points="0,0 80,32 0,64" fill="var(--red)"/></svg>
      <div class="date-text date-month">FEB</div>
      <div class="date-text date-days">18-23</div>
      <div class="date-text date-year">2020</div>
    </div>
    <p class="venue">MESSE WOLKENBACH</p>
    <p class="program">TATTOOS PIERCINGS SHOWS</p>
    <p class="hours">SAMSTAG 12-23 UHR SONNTAG 12-20 UHR</p>
  </section>

</main>
</body>
</html>
```